broucher for electrical contracting buisness

use website template and attached files for colour scheme / ideas

Industry/Entity Type

Electrical

Requirements
Must have
• A5 folded to A4 4 pp format
• use the written content in the broucher word document as a guide

```html
<!DOCTYPE html>
<html lang="en">
<head>
<meta charset="utf-8">
<title>Brayford Electrical – Brochure</title>
<link href="https://fonts.googleapis.com/css2?family=Archivo:wght@500;600;700&family=Open+Sans:wght@400;600;700&display=swap" rel="stylesheet">
<style>
  :root {
    --navy: #1f2a5c;
    --red: #e3171e;
    --ink: #2a2a2a;
    --paper: #ffffff;
    --sheet-grey: #e8e9eb;
    --backdrop: #d6d6d8;
    --rule: #bfc2c9;
  }
  * { box-sizing: border-box; margin: 0; padding: 0; }
  html, body { width: 1200px; height: 3279px; overflow: hidden; }
  body { background: var(--backdrop); font-family: "Open Sans", Arial, sans-serif; color: var(--ink); position: relative; }

  .cover { position: absolute; left: 184px; width: 835px; height: 1078px; background: var(--sheet-grey); overflow: hidden; }
  .cover--front { top: 87px; }
  .cover--back { top: 2105px; }
  .cover__shapes { position: absolute; inset: 0; }

  .brand-name { font-family: "Archivo", Arial, sans-serif; font-weight: 700; letter-spacing: 3px; line-height: 1; color: var(--paper); }
  .cover--front .brand-name { position: absolute; left: 40px; top: 46px; font-size: 50px; }
  .cover--front .brand-name span, .cover--back .brand-name span { display: block; font-size: 50px; }
  .cover--back .brand-name { position: absolute; left: 0; right: 0; top: 52px; text-align: center; font-size: 50px; }

  .photo-ring { position: absolute; border-radius: 50%; background: var(--paper); }
  .photo-ring .photo { position: absolute; inset: 14px; border-radius: 50%; }
  .photo--wiring { background: radial-gradient(circle at 45% 40%, #f3efe9 0%, #c9ccd2 45%, #4a78b5 75%, #8b99a8 100%); }
  .photo--bulb { background: radial-gradient(circle at 40% 40%, #f4f4f4 0%, #d6d6d6 55%, #9a9da2 100%); }

  .headline { position: absolute; left: 318px; width: 490px; top: 805px; text-align: center; font-family: "Archivo", Arial, sans-serif; font-weight: 600; font-size: 52px; line-height: 67px; color: #1a1a1a; }
  .headline em { font-style: normal; color: var(--red); }
  .headline__rule { position: absolute; left: 328px; width: 470px; top: 1006px; height: 3px; background: #222; }
  .web-link { position: absolute; left: 318px; width: 490px; top: 1018px; text-align: center; font-family: "Archivo", Arial, sans-serif; font-weight: 700; font-size: 26px; color: var(--red); }

  .contact { position: absolute; left: 0; right: 0; top: 870px; text-align: center; font-family: "Archivo", Arial, sans-serif; }
  .contact__title { font-size: 44px; font-weight: 700; color: var(--navy); line-height: 60px; }
  .contact__phone { font-size: 36px; font-weight: 600; color: var(--red); line-height: 46px; letter-spacing: 1px; }
  .contact__line { font-family: "Open Sans", Arial, sans-serif; font-size: 22px; color: #222; line-height: 32px; }

  .spread { position: absolute; left: 48px; top: 1246px; width: 1104px; height: 765px; background: var(--paper); display: flex; }
  .page { position: relative; width: 552px; height: 765px; }
  .page + .page { border-left: 1px solid #eee; }

  .page-head { position: absolute; left: 17px; right: 17px; top: 26px; display: flex; align-items: center; gap: 14px; }
  .page-head::before, .page-head::after { content: ""; flex: 1; height: 2px; background: var(--red); }
  .page-head .brand-name { color: var(--navy); font-size: 22px; letter-spacing: 1px; text-align: center; line-height: 1.05; }
  .page-head .brand-name span { display: block; font-size: 12px; letter-spacing: 4px; }

  .body-copy { font-size: 12px; line-height: 17px; text-align: justify; color: #333; }
  .body-copy p + p { margin-top: 12px; }
  .intro { position: absolute; left: 17px; right: 16px; top: 80px; }

  .perks { position: absolute; left: 17px; width: 519px; top: 245px; height: 164px; background: linear-gradient(120deg, var(--navy), #2d3b76); list-style: none; padding: 16px 22px; }
  .perks li { display: flex; align-items: center; gap: 10px; color: var(--paper); font-weight: 700; font-size: 13px; line-height: 27px; }
  .perks svg { width: 15px; height: 15px; flex: none; }

  .section-title { position: absolute; font-family: "Archivo", Arial, sans-serif; font-weight: 700; font-size: 31px; color: var(--red); line-height: 1; padding-bottom: 4px; border-bottom: 3px solid var(--navy); }
  .section-title--residential { left: 17px; top: 440px; }
  .section-title--commercial { left: 14px; top: 82px; }
  .residential-copy { position: absolute; left: 17px; width: 210px; top: 497px; }
  .commercial-copy { position: absolute; left: 14px; right: 15px; top: 393px; }

  .pic { position: absolute; }
  .pic--switchboard { left: 243px; top: 449px; width: 293px; height: 201px; background: linear-gradient(160deg, #3a3a3a, #b23a35 55%, #e7e7e7); }
  .pic--lobby { left: 14px; top: 136px; width: 523px; height: 231px; background: linear-gradient(180deg, #5a5652, #d9d2c8 60%, #8a847c); }
  .pic--corridor { left: 14px; top: 556px; width: 243px; height: 136px; background: linear-gradient(90deg, #c4202a 45%, #e9e6e1); }
  .pic--office { left: 282px; top: 556px; width: 255px; height: 136px; background: linear-gradient(180deg, #d8d4cd, #8d8a85); }

  .page-foot { position: absolute; left: 17px; right: 17px; top: 727px; height: 2px; background: var(--navy); }
  .page-foot__num { position: absolute; left: 50%; top: -11px; transform: translateX(-50%); width: 24px; height: 24px; border-radius: 50%; border: 2px solid var(--navy); background: var(--paper); font-size: 11px; font-weight: 700; text-align: center; line-height: 20px; color: var(--navy); }
  .page-foot__left, .page-foot__right { position: absolute; top: 8px; font-size: 10px; color: #333; }
  .page-foot__left { left: 0; }
  .page-foot__right { right: 0; }
</style>
</head>
<body>

<section class="cover cover--front">
  <svg class="cover__shapes" viewBox="0 0 835 1078" aria-hidden="true">
    <polygon points="0,0 565,0 120,1078 0,1078" fill="var(--navy)"/>
    <polygon points="620,0 668,0 238,1078 178,1078" fill="var(--navy)"/>
  </svg>
  <div class="brand-name">BRAYFORD<span>ELECTRICAL</span></div>
  <div class="photo-ring" style="left:122px; top:262px; width:464px; height:464px;">
    <div class="photo photo--wiring" role="img" aria-label="Electrician testing wiring in a fuse board with a red screwdriver"></div>
  </div>
  <h1 class="headline">WE <em>PRIDE</em><br>OURSELVES ON<br>PROVIDING <em>YOU</em></h1>
  <div class="headline__rule"></div>
  <div class="web-link">www.brayfordelectrical.com</div>
</section>

<section class="spread">
  <article class="page">
    <header class="page-head"><div class="brand-name">BRAYFORD<span>ELECTRICAL</span></div></header>
    <div class="intro body-copy">
      <p>Providing you with high quality electrical componentry and proven industry know how, at Brayford Electrical you can rest assured your job will be completed to standard and on time. We pride ourselves on providing you with professional electrical services at competitive prices.</p>
      <p>With a qualified workforce, fleet of specialist vehicles, modern plant and equipment, Brayford Electrical provides cost efficient and innovative electrical solutions to a wide range of clients and industries.</p>
    </div>
    <ul class="perks">
      <li><svg viewBox="0 0 16 16"><circle cx="8" cy="8" r="7" fill="none" stroke="var(--red)" stroke-width="2"/><path d="M4.5 8.2l2.3 2.3 4.6-4.8" fill="none" stroke="var(--red)" stroke-width="2"/></svg>15% discount on labour if you are a pensioner</li>
      <li><svg viewBox="0 0 16 16"><circle cx="8" cy="8" r="7" fill="none" stroke="var(--red)" stroke-width="2"/><path d="M4.5 8.2l2.3 2.3 4.6-4.8" fill="none" stroke="var(--red)" stroke-width="2"/></svg>24/7 call outs</li>
      <li><svg viewBox="0 0 16 16"><circle cx="8" cy="8" r="7" fill="none" stroke="var(--red)" stroke-width="2"/><path d="M4.5 8.2l2.3 2.3 4.6-4.8" fill="none" stroke="var(--red)" stroke-width="2"/></svg>Quality guarantee on all works</li>
      <li><svg viewBox="0 0 16 16"><circle cx="8" cy="8" r="7" fill="none" stroke="var(--red)" stroke-width="2"/><path d="M4.5 8.2l2.3 2.3 4.6-4.8" fill="none" stroke="var(--red)" stroke-width="2"/></svg>Manufacturer's warranty on all products</li>
      <li><svg viewBox="0 0 16 16"><circle cx="8" cy="8" r="7" fill="none" stroke="var(--red)" stroke-width="2"/><path d="M4.5 8.2l2.3 2.3 4.6-4.8" fill="none" stroke="var(--red)" stroke-width="2"/></svg>Locally owned and run business</li>
    </ul>
    <h2 class="section-title section-title--residential">RESIDENTIAL</h2>
    <div class="residential-copy body-copy">
      <p>We cover a large variety of domestic work W.A wide. We take pride in each and every job that we do and treat it as if it were our own home. Due to our vast experience in the domestic field we can inform our clients with the most cost efficient and beneficial ideas. At Brayford Electrical no one is treated like just a number; each client is extremely important to us.</p>
    </div>
    <div class="pic pic--switchboard" role="img" aria-label="Residential switchboard with circuit breakers and red wiring"></div>
    <footer class="page-foot">
      <span class="page-foot__num">02</span>
      <span class="page-foot__left">info@brayfordelectrical.com</span>
      <span class="page-foot__right">www.brayfordelectrical.com</span>
    </footer>
  </article>

  <article class="page">
    <header class="page-head"><div class="brand-name">BRAYFORD<span>ELECTRICAL</span></div></header>
    <h2 class="section-title section-title--commercial">COMMERCIAL</h2>
    <div class="pic pic--lobby" role="img" aria-label="Modern commercial lobby lit with ceiling downlights"></div>
    <div class="commercial-copy body-copy">
      <p>We provide our commercial clients with top quality products and services that are delivered on time and to budget. We pledge to provide all of this and more without compromising on quality. All our goods and services are warrantied, and our team will always work to deliver exceptional services and long-lasting electrical work.</p>
      <p>When you need lighting for warehouses or offices, security or exit lighting we will have the solution. Our team of qualified electricians have access to an extensive range of lighting products. We can install your lighting, or design a lighting solution for your project, large or small.</p>
    </div>
    <div class="pic pic--corridor" role="img" aria-label="Office corridor with red wall panels and bright lighting"></div>
    <div class="pic pic--office" role="img" aria-label="Open office interior with recessed ceiling lights"></div>
    <footer class="page-foot">
      <span class="page-foot__num">03</span>
      <span class="page-foot__left">info@brayfordelectrical.com</span>
      <span class="page-foot__right">www.brayfordelectrical.com</span>
    </footer>
  </article>
</section>

<section class="cover cover--back">
  <svg class="cover__shapes" viewBox="0 0 835 1078" aria-hidden="true">
    <polygon points="0,0 835,0 835,240 0,780" fill="var(--navy)"/>
    <polygon points="835,262 835,300 0,840 0,802" fill="var(--paper)"/>
  </svg>
  <div class="brand-name">BRAYFORD<span>ELECTRICAL</span></div>
  <div class="photo-ring" style="left:116px; top:196px; width:538px; height:538px;">
    <div class="photo photo--bulb" role="img" aria-label="Light bulb figure plugging a cable into a wall socket"></div>
  </div>
  <div class="contact">
    <div class="contact__title">Contact Us</div>
    <div class="contact__phone">012 555 01890</div>
    <div class="contact__line">info@brayfordelectrical.com</div>
    <div class="contact__line">www.brayfordelectrical.com</div>
  </div>
</section>

</body>
</html>
```